Marketing / Informational Site for Marriage and Family Therapists Cooperative

We need a web design for a new Marriage and Family Therapist Cooperative, called Meadowgate Counselors. This is a market and information site for potential clients and referrals to learn more about the team and get contact information.

We are looking for profession, clean, and modern design, that cater towards families and mom's concerned about their families mental health and child development.

This should include a home page, an general about page, 3 bio pages (1 for each therapist listed below), and a general contact us page.

Our Domain Name

Meadowgatecounselors.example

Company Name

Meadowgate Counselors

Group Moto/Philosophy

“Our sorrows and wounds are healed only when we touch them with compassion.” - Orvelan

Our Logo

See Heron Final (attached)

Home Page (Introduction)

Feeling stressed and overwhelmed?
Encountering barriers towards your goals?
Having difficulty accomplishing the simplest task?
Have the need to talk but unsure who to turn to?

Therapy can assist you in overcoming all of these challenges. Assist you in uncovering the difficulties and barriers that are keeping you from achieving your life’s ambitions, help discover ways to overcome them, and cope with the impact your behaviour has on your occupation, personal life and social life.

Welcome to our practice, with over 20 years of combined experience in the clinical field you are sure to find the right fit for your needs. Each clinician has experience working with groups, adults, teens, children, families, and couples. We specialize in fostering healthy relationships between individuals, managing depression and anxiety, overcoming trauma, and developing occupational success. Feel free to explore information about each clinician and make an appointment with one of us today.

About Us (bio pics attached)

Marisel Dunkworth

My name is Dr. MariSel Dunkworth and I am a Licensed Marriage Family Therapist with a practice in Riverside, CA. I have devoted my life’s work into developing my skills in this profession. I have over 15 years of experience working in the clinical and the social service settings. These years have afforded me the opportunity to work with groups, families, adults, teens and children with varying symptoms. I have helped clients that have trauma, abuse histories, and many within the legal or social service systems. I enjoy working individuals from all walks of life achieve self sufficiency, social success and occupational success. In my years of training I have come to develop a culturally sensitive practice that centers around the needs of the client.

I have held many positions in my clinical career beginning as clinician moving upwards toward supervisor and program coordinator. I have also over 5 years of experience as an adjunct faculty member in the University setting teaching student to become Marriage and Family Therapists. As a clinician I focused on enriching my clinical skills by developing outcome driven practices to achieve client’s desired goals. As a clinical supervisor, I guided clinicians along their own paths towards clinical licensure. As a program coordinator, I helped develop a clinical assessment and triage program from ground up to assist client in accessing services in the South Los Angeles Area. The program would assist over 100 plus clients on a monthly basis get connected to clinical services and linked to any additional resources as needed by the individual. I have graduated with my, Bachelor’s degree at the Halvern College, Riverside. I received my Masters degree in Clinical Psychology at Mount St. Mary’s University, and my Doctorate degree in Clinical Psychology at Tamsworth Institute.

To schedule an appointment with Dr. MariSel Dunkworth, LMFT:

email: marisel582@postbox.example
Phone: (951)555-0182

Jeb Kowal

My name is Rosalindra (Jeb) Kowal, I received my Masters Degree of Counseling in Marriage and Family Therapy from Corvell Bay State College in June 2000. I have acquired over 15 years of experience helping Individuals, Couples, and Families cope with issues of Anxiety, Depression, Grief and Bereavement, and HIV/AIDS.

I am a Family Systems Therapist and I truly believe the dynamics in our family of origin greatly shape our current belief systems and behaviors. However, I often utilize a variety of approaches to help my clients achieve their goals depending on their individual needs.

My greatest strength as a Marriage and Family Therapist is helping my clients explore ways to make the changes in their lives that will allow them to live their life to their fullest potential. I help my clients achieve their personal life goals with a warm, safe, non-judgmental , and supportive environment. In doing so, my clients are encouraged to explore the issues that may be preventing them from living the life they desire. Thus, empowering them to take control of their personal journey to living a productive and meaningful life.

If you feel that you are ready to commit to bringing about positive changes in your life and would like support in exploring this path, I’m here to work with you in your journey to personal growth and development.

To schedule an appointment with Rosalindra Kowal, LMFT:

e-mail: rkjeb7@mailnest.example
Phone: (951)555-0147

Dena Holcroft

Dena Holcroft graduated with a Masters in Marriage and Family Therapy from Pellridge Crestwood College. She currently holds a license in Marriage and Family Therapy in the State of California. She is also formally trained in Clinical Art Therapy. Dena's expertise lies in providing treatment to individuals experiencing work-related injuries, severe physical and emotional pain, trauma, grief and loss, anxiety and depression. In her early career, she provided valuable service at the largest free clinic in the nation serving marginalized families and children. For the past ten years, Dena has worked with HIV/AIDS population.
Dena comes from a multicultural background and she has utilized this experience and knowledge in serving a variety of populations. At an organizational level, Dena has worked extensively with challenging issues such as the chemical dependency and homelessness. In her private practice, Dena is proficient in working within individuals experiencing relationship concerns, marital and family conflict, depression/anxiety, self-esteem concerns, adjustment disorders, and pain management. She has treated clients from diverse cultural, linguistic backgrounds and sexual orientations.
Dena is trained in Family Systems Theory and incorporates other strategies appropriate for each presenting issue. She specializes in Clinical Art Therapy and has successfully utilized an integrated approach including guided imagery and relaxation skills training for many years.

To schedule an appointment with Dena Holcroft, LMFT

e-mail: greypinestudio@inkmail.example
Phone: (951) 555-0169

Target Market(s)

Families with child development, marriage issues, or other mental health needs

Industry/Entity Type

Marketing

Number of Pages Required

5+ page

Requirements
Must have
• 1 home page, 1 about page, 1 contact page. About page could either be standalone page with 3 different bio pages for each therapist or an all in one about page that includes bios for all 3 therapists.

```html
<!DOCTYPE html>
<html lang="en">
<head>
<meta charset="utf-8">
<title>Meadowgate Counselors</title>
<link href="https://fonts.googleapis.com/css2?family=Ubuntu:wght@300;400;500;700&display=swap" rel="stylesheet">
<style>
:root{
  --green:#8db635;
  --green-dark:#74a02a;
  --band:#b7cd6f;
  --blue:#4a9fd6;
  --ink:#4a4a4a;
  --muted:#8a8a8a;
  --rule:#e3e3e3;
  --charcoal:#5a5a5a;
  --footer:#3b3b3b;
  --footer-deep:#2f2f2f;
  --white:#ffffff;
}
*{box-sizing:border-box;margin:0;padding:0}
html,body{width:733px;height:1200px;overflow:hidden;background:var(--white)}
body{font-family:"Ubuntu",Arial,sans-serif;color:var(--ink);position:relative}
.page{position:relative;width:733px;height:1200px;overflow:hidden}

/* header */
.site-header{position:absolute;top:0;left:0;width:733px;height:36px;background:var(--white);display:flex;align-items:center;padding:0 14px 0 22px}
.brand{display:flex;align-items:center;gap:6px;font-size:10px;font-weight:500;color:var(--green-dark)}
.brand-dot{width:12px;height:12px;border-radius:50%;background:var(--green)}
.main-nav{margin-left:auto;display:flex;align-items:center;gap:22px;font-size:7px;letter-spacing:.4px;color:var(--ink)}
.main-nav .active{color:var(--green);border-bottom:2px solid var(--green);padding-bottom:3px}
.btn-small{font-size:6.5px;color:var(--white);padding:4px 8px;border-radius:2px;letter-spacing:.4px}
.btn-login{background:var(--green);margin-left:4px}
.btn-register{background:var(--blue);margin-left:-14px}

/* hero */
.hero{position:absolute;top:36px;left:0;width:733px;height:310px;background:linear-gradient(100deg,#6e6a66 0%,#a19b95 45%,#cfcac3 75%,#b9b3ac 100%)}
.hero-text{position:absolute;left:38px;top:92px;color:var(--white)}
.hero-quote{font-size:22px;font-weight:500;line-height:1.15}
.hero-quote span{display:block;font-size:16px;font-weight:400;margin-top:4px}
.hero-author{font-size:7px;margin-top:6px;opacity:.9}
.btn-read{display:inline-block;margin-top:12px;background:var(--green);color:var(--white);font-size:7px;padding:7px 12px;border-radius:2px;letter-spacing:.5px}
.hero-arrow{position:absolute;top:140px}
.hero-curve{position:absolute;left:0;bottom:0}

/* team */
.team{position:absolute;top:364px;left:0;width:733px;display:flex;justify-content:center;gap:12px}
.team-card{width:48px;text-align:center}
.team-photo{width:48px;height:48px;border:3px solid var(--white);box-shadow:0 1px 3px rgba(0,0,0,.25);background:linear-gradient(160deg,#9f8674,#5f4c42)}
.team-name{font-size:4.5px;color:var(--muted);margin-top:4px}

/* welcome */
.welcome{position:absolute;top:440px;left:0;width:733px;text-align:center}
.section-title{display:flex;align-items:center;justify-content:center;gap:10px;font-size:11px;color:var(--green);letter-spacing:.4px}
.section-title::before,.section-title::after{content:"";width:34px;height:1px;background:var(--rule)}
.welcome-intro{width:560px;margin:10px auto 0;font-size:5px;line-height:1.6;color:var(--muted)}
.concerns{display:grid;grid-template-columns:200px 200px;gap:6px 30px;width:430px;margin:14px auto 0;text-align:left}
.concern{display:flex;align-items:center;gap:5px;font-size:6.2px;color:var(--green-dark)}

/* services */
.services{position:absolute;top:557px;left:0;width:733px;height:282px;background:var(--band)}
.services .section-title{margin-top:26px;color:var(--white)}
.services .section-title::before,.services .section-title::after{background:rgba(255,255,255,.6)}
.service-list{display:flex;justify-content:center;gap:28px;margin-top:32px}
.service{width:128px;text-align:center;color:var(--white)}
.service-icon{width:50px;height:50px;border-radius:50%;background:var(--charcoal);border:3px solid rgba(255,255,255,.7);margin:0 auto;display:flex;align-items:center;justify-content:center}
.service-name{font-size:6px;letter-spacing:.4px;margin-top:10px}
.service-text{font-size:5px;line-height:1.6;margin-top:5px;opacity:.95}
.band-arrow{position:absolute;top:128px}

/* about + testimonials */
.about{position:absolute;top:856px;left:22px;width:340px}
.block-title{font-size:12px;color:var(--green);letter-spacing:.3px;padding-bottom:5px;border-bottom:1px solid var(--rule)}
.about-text{font-size:5.2px;line-height:1.7;color:var(--muted);margin-top:8px}
.btn-book{display:inline-block;margin-top:12px;background:var(--green);color:var(--white);font-size:6px;padding:6px 11px;border-radius:2px}
.testimonials{position:absolute;top:856px;left:395px;width:316px}
.testimonials .block-title{text-align:center}
.testimonial{display:flex;gap:12px;margin-top:10px}
.client-photo{flex:none;width:52px;height:52px;background:linear-gradient(150deg,#8c7a6b,#3f3833)}
.quote-text{font-size:5.2px;line-height:1.7;color:var(--muted)}
.quote-name{font-size:5.5px;color:var(--ink);margin-top:6px;font-weight:500}
.quote-role{font-size:5px;color:var(--muted)}

/* footer */
.site-footer{position:absolute;top:1100px;left:0;width:733px;height:100px;background:var(--footer);color:#cfcfcf}
.footer-cols{display:flex;gap:0;padding:10px 22px 0}
.footer-col{width:100px}
.footer-col h4{font-size:5.5px;color:var(--white);font-weight:500;letter-spacing:.4px;margin-bottom:5px}
.footer-col li{list-style:none;font-size:4.8px;line-height:1.9;color:#b9b9b9}
.newsletter{width:150px;margin-left:20px}
.newsletter p{font-size:4.8px;color:#b9b9b9}
.newsletter .field{width:110px;height:12px;background:var(--white);margin-top:6px;font-size:4.5px;color:#999;padding:3px 5px}
.newsletter .btn-sub{display:inline-block;margin-top:5px;background:var(--footer-deep);border:1px solid #666;font-size:4.8px;color:var(--white);padding:3px 7px}
.follow{margin-left:auto;width:80px}
.social{display:flex;align-items:center;gap:6px;font-size:4.8px;color:#b9b9b9;margin-bottom:5px}
.social i{width:11px;height:11px;border-radius:50%;background:#666;display:block}
.copyright{position:absolute;bottom:0;left:0;width:733px;height:15px;background:var(--footer-deep);font-size:4.8px;color:#9a9a9a;text-align:center;line-height:15px}
</style>
</head>
<body>
<div class="page">

  <header class="site-header">
    <div class="brand"><span class="brand-dot"></span>Meadowgate Counselors</div>
    <nav class="main-nav">
      <span class="active">HOME</span>
      <span>ABOUT US</span>
      <span>THERAPISTS</span>
      <span>CONTACT US</span>
      <span class="btn-small btn-login">LOG IN</span>
      <span class="btn-small btn-register">REGISTER</span>
    </nav>
  </header>

  <section class="hero">
    <div class="hero-bg" role="img" aria-label="Photo of a counselling session in a calm, bright room" style="position:absolute;inset:0"></div>
    <svg class="hero-arrow" style="left:10px" width="10" height="16" viewBox="0 0 10 16"><path d="M8 2 2 8l6 6" fill="none" stroke="#fff" stroke-width="1.6"/></svg>
    <svg class="hero-arrow" style="right:10px" width="10" height="16" viewBox="0 0 10 16"><path d="M2 2l6 6-6 6" fill="none" stroke="#fff" stroke-width="1.6"/></svg>
    <div class="hero-text">
      <p class="hero-quote">Our sorrows and wounds are healed only<span>when we touch them with compassion.”</span></p>
      <p class="hero-author">- Orvelan</p>
      <span class="btn-read">READ MORE</span>
    </div>
    <svg class="hero-curve" width="733" height="40" viewBox="0 0 733 40" preserveAspectRatio="none"><path d="M0 40 L0 30 Q366 -10 733 30 L733 40 Z" fill="#fff"/></svg>
  </section>

  <section class="team">
    <div class="team-card"><div class="team-photo" role="img" aria-label="Portrait of therapist Marisel Dunkworth"></div><p class="team-name">Marisel Dunkworth</p></div>
    <div class="team-card"><div class="team-photo" role="img" aria-label="Portrait of therapist Jeb Kowal"></div><p class="team-name">Jeb Kowal</p></div>
    <div class="team-card"><div class="team-photo" role="img" aria-label="Portrait of therapist Dena Holcroft"></div><p class="team-name">Dena Holcroft</p></div>
  </section>

  <section class="welcome">
    <h2 class="section-title">WELCOME TO OUR COMPANY</h2>
    <p class="welcome-intro">Therapy can assist you in overcoming all of these challenges. It helps uncover the difficulties and barriers that keep you from achieving your ambitions, discover ways to overcome them, and cope with the impact your behaviour has on your occupation, personal life and social life.</p>
    <div class="concerns">
      <p class="concern"><svg width="7" height="7" viewBox="0 0 8 8"><path d="M1 4l2 2 4-5" fill="none" stroke="#8db635" stroke-width="1.4"/></svg>Feeling stressed and overwhelmed?</p>
      <p class="concern"><svg width="7" height="7" viewBox="0 0 8 8"><path d="M1 4l2 2 4-5" fill="none" stroke="#8db635" stroke-width="1.4"/></svg>Having difficulty accomplishing the simplest task?</p>
      <p class="concern"><svg width="7" height="7" viewBox="0 0 8 8"><path d="M1 4l2 2 4-5" fill="none" stroke="#8db635" stroke-width="1.4"/></svg>Encountering barriers towards your goals?</p>
      <p class="concern"><svg width="7" height="7" viewBox="0 0 8 8"><path d="M1 4l2 2 4-5" fill="none" stroke="#8db635" stroke-width="1.4"/></svg>Have the need to talk but unsure who to turn to?</p>
    </div>
  </section>

  <section class="services">
    <h2 class="section-title">OUR SERVICES</h2>
    <svg class="band-arrow" style="left:12px" width="10" height="16" viewBox="0 0 10 16"><path d="M8 2 2 8l6 6" fill="none" stroke="#fff" stroke-width="1.6"/></svg>
    <svg class="band-arrow" style="right:12px" width="10" height="16" viewBox="0 0 10 16"><path d="M2 2l6 6-6 6" fill="none" stroke="#fff" stroke-width="1.6"/></svg>
    <div class="service-list">
      <div class="service">
        <div class="service-icon"><svg width="20" height="16" viewBox="0 0 20 16"><circle cx="6" cy="4" r="3" fill="#fff"/><circle cx="14" cy="4" r="3" fill="#fff"/><path d="M0 16c0-5 3-7 6-7s6 2 6 7zM8 16c0-5 3-7 6-7s6 2 6 7z" fill="#fff"/></svg></div>
        <p class="service-name">FAMILY THERAPY</p>
        <p class="service-text">We help families build healthy bonds, ease conflict and support every member through change.</p>
      </div>
      <div class="service">
        <div class="service-icon"><svg width="18" height="16" viewBox="0 0 18 16"><path d="M9 15S1 10 1 5a4 4 0 0 1 8-1 4 4 0 0 1 8 1c0 5-8 10-8 10z" fill="#fff"/></svg></div>
        <p class="service-name">COUPLES THERAPY</p>
        <p class="service-text">Partners learn to listen, rebuild trust and find new ways through marital concerns.</p>
      </div>
      <div class="service">
        <div class="service-icon"><svg width="16" height="16" viewBox="0 0 16 16"><circle cx="8" cy="4" r="3.2" fill="#fff"/><path d="M2 16c0-5 3-7 6-7s6 2 6 7z" fill="#fff"/></svg></div>
        <p class="service-name">CHILD THERAPY</p>
        <p class="service-text">Caring support for children and teens facing anxiety, grief or developmental worries.</p>
      </div>
      <div class="service">
        <div class="service-icon"><svg width="16" height="16" viewBox="0 0 16 16"><circle cx="8" cy="8" r="6.5" fill="none" stroke="#fff" stroke-width="2"/><circle cx="8" cy="8" r="2.5" fill="#fff"/></svg></div>
        <p class="service-name">ADULT THERAPY</p>
        <p class="service-text">Individual sessions for depression, trauma, stress and occupational success.</p>
      </div>
    </div>
  </section>

  <section class="about">
    <h3 class="block-title">ABOUT US</h3>
    <p class="about-text">Welcome to our practice. With over 20 years of combined experience in the clinical field you are sure to find the right fit for your needs. Each clinician has experience working with groups, adults, teens, children, families and couples. We specialize in fostering healthy relationships between individuals, managing depression and anxiety, overcoming trauma, and developing occupational success. Our team offers a warm, safe, non-judgmental and supportive environment where every client is heard. Feel free to explore information about each clinician and make an appointment with one of us today.</p>
    <span class="btn-book">Book now</span>
  </section>

  <section class="testimonials">
    <h3 class="block-title">TESTIMONIALS</h3>
    <div class="testimonial">
      <div class="client-photo" role="img" aria-label="Photo of a satisfied client"></div>
      <div>
        <p class="quote-text">“Working with this team changed how our family talks to one another. We felt listened to from the very first session, and the tools we learned still help us every week. I recommend them to anyone who is ready for change.”</p>
        <p class="quote-name">MR. CALDER VOSS</p>
        <p class="quote-role">Client, Riverside</p>
      </div>
    </div>
  </section>

  <footer class="site-footer">
    <div class="footer-cols">
      <div class="footer-col"><h4>INFORMATION</h4><ul><li>Home</li><li>About us</li><li>Therapists</li><li>Contact us</li></ul></div>
      <div class="footer-col"><h4>PRODUCTS</h4><ul><li>Family sessions</li><li>Couples care</li><li>Child support</li><li>Group work</li></ul></div>
      <div class="footer-col"><h4>INFORMATION</h4><ul><li>Search</li><li>Blog</li><li>Resources</li><li>Site map</li></ul></div>
      <div class="newsletter"><h4 class="footer-col" style="width:auto;font-size:5.5px;color:#fff;font-weight:500;margin-bottom:5px">NEWSLETTER SIGNUP</h4><p>Get our latest updates through your email</p><div class="field">Enter your email</div><span class="btn-sub">SUBSCRIBE</span></div>
      <div class="follow footer-col"><h4>FOLLOW US</h4>
        <p class="social"><i></i>Feedline</p>
        <p class="social"><i></i>Chirpwire</p>
        <p class="social"><i></i>Linkwell</p>
      </div>
    </div>
    <p class="copyright">© 2015 Meadowgate Counselors. All Rights Reserved</p>
  </footer>

</div>
</body>
</html>
```